Business card for communications

Need a business card for my consulting business - I work with not for profits, start ups and social enterprises on their media, communications campaigns.

Please see my website for colours, images and fonts www.morelbratton.example

Dana Morelbrat
Communications & Campaign strategist
Sydney - Melbourne
M: 0498 317 026
E: dana@morelbratton.example
S: danamorelbrat
W: morelbratton.example
T: @danamorelbrat

(above is info only and can be presented any way e.g. should not have to be M for mobile - it should be an icon)
Updates

Dear designers I have updated the brief and uploaded high res images from my website for you to use. The designs so far with the use of images and icons are much better so far. Thank you I look forward to receiving your revised designs. Dana Morelbrat

Industry/Entity Type

Communications

Font styles to use
Sans Serif

Requirements
Must have
• Icons for contact details
Images from the website www.morelbratton.example
Nice to have
• Images - attached

```html
<!DOCTYPE html>
<html lang="en">
<head>
<meta charset="utf-8">
<title>Dana Morelbrat – Business Card</title>
<link href="https://fonts.googleapis.com/css2?family=Noto+Sans:wght@400;500&display=swap" rel="stylesheet">
<style>
  :root {
    --stage: #808080;
    --card-white: #ffffff;
    --brand-yellow: #ffd200;
    --ink: #111111;
    --nav-ink: #222222;
    --nav-active: #f2c200;
    --handle-blue: #2aa3e0;
    --photo-dark: #6b4a2c;
    --photo-mid: #a8794c;
    --photo-light: #c9a57c;
  }
  * { box-sizing: border-box; margin: 0; padding: 0; }
  html, body {
    width: 1200px; height: 532px; overflow: hidden;
    background: var(--stage);
    font-family: "Noto Sans", Verdana, sans-serif;
    color: var(--ink);
  }
  .stage { position: relative; width: 1200px; height: 532px; }

  .card {
    position: absolute; top: 86px;
    width: 570px; height: 360px;
    background: var(--card-white);
    overflow: hidden;
    box-shadow: 0 3px 8px rgba(0,0,0,0.3);
  }
  .card--front { left: 20px; }
  .card--back { left: 610px; }

  /* Front */
  .site-header {
    position: absolute; top: 0; left: 0; right: 0; height: 52px;
    display: flex; justify-content: space-between; align-items: flex-end;
    padding: 6px 16px 8px 14px;
  }
  .site-name { font-size: 21px; line-height: 1; font-weight: 400; }
  .site-tagline { font-size: 10.5px; font-weight: 500; margin-top: 2px; }
  .site-nav { display: flex; gap: 16px; font-size: 9px; text-transform: uppercase; color: var(--nav-ink); padding-bottom: 4px; }
  .site-nav .is-active { color: var(--nav-active); }

  .hero-photo {
    position: absolute; top: 52px; left: 0; right: 0; height: 200px;
    background: linear-gradient(135deg, var(--photo-dark) 0%, var(--photo-mid) 45%, var(--photo-light) 70%, var(--photo-mid) 100%);
  }

  .contact-band {
    position: absolute; top: 252px; left: 0; right: 0; bottom: 0;
    background: var(--brand-yellow);
    display: flex; justify-content: space-around; align-items: flex-start;
    padding: 14px 30px 0;
  }
  .contact-item { display: flex; flex-direction: column; align-items: center; gap: 10px; font-size: 11px; }
  .contact-icon { width: 40px; height: 40px; border-radius: 50%; background: var(--card-white); display: flex; align-items: center; justify-content: center; }

  /* Back */
  .corner { position: absolute; }
  .corner--top { top: 0; left: 0; }
  .corner--bottom { right: 0; bottom: 0; }
  .card-name {
    position: absolute; left: 0; right: 0; top: 118px;
    text-align: center; font-size: 50px; font-weight: 400; letter-spacing: 0.5px;
  }
  .handles {
    position: absolute; left: 0; right: 0; top: 270px;
    display: flex; justify-content: center; gap: 14px; font-size: 14px;
  }
  .handle { display: flex; align-items: center; gap: 6px; }
  .handle-mark { width: 18px; height: 18px; border-radius: 50%; background: var(--handle-blue); }
</style>
</head>
<body>
<div class="stage">

  <section class="card card--front">
    <header class="site-header">
      <div class="site-brand">
        <div class="site-name">Dana Morelbrat</div>
        <div class="site-tagline">Communications &amp; Campaign strategist</div>
      </div>
      <nav class="site-nav">
        <span class="is-active">Home</span>
        <span>About Dana</span>
        <span>Services</span>
        <span>Clients</span>
        <span>Contact</span>
      </nav>
    </header>

    <div class="hero-photo" role="img" aria-label="Overhead photo of a shared wooden desk with laptops, keyboards, papers and coffee cups"></div>

    <div class="contact-band">
      <div class="contact-item">
        <span class="contact-icon">
          <svg width="22" height="22" viewBox="0 0 24 24" aria-hidden="true">
            <path d="M3 9c0-3 4-4 9-4s9 1 9 4v2h-5V9H8v2H3z" fill="#ffd200"/>
            <rect x="6" y="12" width="12" height="8" rx="1.5" fill="#ffd200"/>
            <circle cx="12" cy="16" r="2" fill="#fff"/>
          </svg>
        </span>
        <span>0498 317 026</span>
      </div>
      <div class="contact-item">
        <span class="contact-icon">
          <svg width="22" height="22" viewBox="0 0 24 24" aria-hidden="true" fill="none" stroke="#ffd200" stroke-width="1.8">
            <circle cx="12" cy="12" r="9"/>
            <ellipse cx="12" cy="12" rx="4" ry="9"/>
            <line x1="3" y1="12" x2="21" y2="12"/>
          </svg>
        </span>
        <span>dana@morelbratton.example</span>
      </div>
      <div class="contact-item">
        <span class="contact-icon">
          <svg width="22" height="22" viewBox="0 0 24 24" aria-hidden="true">
            <rect x="3" y="6" width="18" height="12" rx="1" fill="#ffd200"/>
            <path d="M3 6l9 7 9-7" fill="none" stroke="#fff" stroke-width="1.4"/>
          </svg>
        </span>
        <span>morelbratton.example</span>
      </div>
    </div>
  </section>

  <section class="card card--back">
    <svg class="corner corner--top" width="150" height="150" viewBox="0 0 150 150" aria-hidden="true">
      <polygon points="0,0 150,0 0,150" fill="var(--brand-yellow)"/>
    </svg>
    <svg class="corner corner--bottom" width="140" height="140" viewBox="0 0 140 140" aria-hidden="true">
      <polygon points="140,0 140,140 0,140" fill="var(--brand-yellow)"/>
    </svg>

    <h1 class="card-name">Dana Morelbrat</h1>

    <div class="handles">
      <span class="handle"><span class="handle-mark"></span>danamorelbrat</span>
      <span class="handle"><span class="handle-mark"></span>@danamorelbrat</span>
    </div>
  </section>

</div>
</body>
</html>
```